Life Coaching and Personal Development Business. Needs Business Card with Logo

We are a Life Coaching and Personal Development Business based in Melbourne, Victoria. We specialise in assisting Individuals who find themselves at cross roads due to career, relationships or just life experiences that are preventing them from having extraordinary lives in happiness, finance or relationships or just being disconnected from a sense of purpose. Our motto is "we help you get there".

Reason: I am awaiting final concepts from a couple of designers

Reason: Deadline passed so now would like to see more options.

Target Market(s)

Individuals who want to move through the cross roads and who are aware that they require help to do so. They are seeking happy, for filing lives through all aspects career, relationships, family and finance

Industry/Entity Type

Finance

Font styles to use
Script

Requirements
Must have
• logo which is representative of moving forward
Business Name: KD Open Horizons
ABN: 5836017294

I do not have a preference with colour but I do not want red orange or green

Should not have
• The card must not be to busy.

```html
<!DOCTYPE html>
<html lang="en">
<head>
<meta charset="utf-8">
<title>KD Open Horizons – Business Card</title>
<link href="https://fonts.googleapis.com/css2?family=Lato:wght@400;700;900&display=swap" rel="stylesheet">
<style>
  :root {
    --bg: #ece9e4;
    --card: #ffffff;
    --card-shade: #f3f3f3;
    --yellow: #e6d46e;
    --blue: #5b8fd6;
    --teal: #2db9c9;
    --ink: #4d4d4d;
    --ink-soft: #6e6e6e;
    --quote-open: #e0c44f;
    --quote-close: #2db9c9;
    --mark: #b7dfe6;
    --white: #ffffff;
  }
  * { margin: 0; padding: 0; box-sizing: border-box; }
  html, body { width: 1200px; height: 1024px; overflow: hidden; }
  body {
    background: var(--bg);
    font-family: "Lato", Arial, sans-serif;
    position: relative;
  }
  .card {
    position: absolute;
    top: 162px;
    width: 400px;
    height: 700px;
    border-radius: 6px;
    overflow: hidden;
    box-shadow: 0 10px 28px rgba(0,0,0,0.16);
  }
  /* Front */
  .card-front {
    left: 150px;
    background: linear-gradient(160deg, var(--card), var(--card-shade));
  }
  .edge {
    position: absolute;
    top: 0;
    width: 26px;
    height: 100%;
    display: flex;
    flex-direction: column;
  }
  .edge span { flex: 1; }
  .edge-left { left: 0; }
  .edge-right { right: 0; }
  .yellow { background: var(--yellow); }
  .blue { background: var(--blue); }
  .teal { background: var(--teal); }

  .brand {
    position: absolute;
    top: 150px;
    left: 0;
    width: 100%;
    display: flex;
    flex-direction: column;
    align-items: center;
  }
  .brand-dot {
    width: 120px;
    height: 120px;
    border-radius: 50%;
    background: var(--mark);
    margin-bottom: 34px;
  }
  .brand-name {
    font-weight: 900;
    font-size: 34px;
    color: var(--ink);
    letter-spacing: 0.2px;
  }
  .tagline {
    position: absolute;
    top: 470px;
    left: 0;
    width: 100%;
    text-align: center;
    font-size: 27px;
    color: var(--ink-soft);
  }
  .tagline .q-open { color: var(--quote-open); font-weight: 900; }
  .tagline .q-close { color: var(--quote-close); font-weight: 900; }

  /* Back */
  .card-back {
    left: 650px;
    background: var(--card);
    display: flex;
    flex-direction: column;
  }
  .back-top { flex: 0 0 320px; background: linear-gradient(160deg, var(--card), var(--card-shade)); }
  .band {
    display: flex;
    flex-direction: column;
    align-items: center;
    justify-content: center;
    gap: 14px;
    color: var(--white);
    font-size: 22px;
    letter-spacing: 0.4px;
  }
  .band-yellow { flex: 0 0 100px; background: var(--yellow); }
  .band-blue { flex: 0 0 130px; background: var(--blue); }
  .band-teal { flex: 1; background: var(--teal); }
  .band svg { display: block; }
  .abn-label { font-weight: 700; margin-right: 8px; }
</style>
</head>
<body>
  <section class="card card-front" aria-label="Business card front">
    <div class="edge edge-left"><span class="yellow"></span><span class="blue"></span><span class="teal"></span></div>
    <div class="edge edge-right"><span class="teal"></span><span class="blue"></span><span class="yellow"></span></div>
    <div class="brand">
      <div class="brand-dot"></div>
      <div class="brand-name">KD Open Horizons</div>
    </div>
    <p class="tagline"><span class="q-open">&ldquo;</span> We help you get there <span class="q-close">&rdquo;</span></p>
  </section>

  <section class="card card-back" aria-label="Business card back">
    <div class="back-top"></div>
    <div class="band band-yellow"></div>
    <div class="band band-blue">
      <p class="abn"><span class="abn-label">ABN</span>5836017294</p>
    </div>
    <div class="band band-teal">
      <svg width="34" height="24" viewBox="0 0 34 24" aria-hidden="true">
        <rect x="1" y="1" width="32" height="22" rx="2" fill="#ffffff"/>
        <path d="M2 3 L17 14 L32 3" fill="none" stroke="#2db9c9" stroke-width="2"/>
      </svg>
      <span class="email">hello@kdopenhorizons.com.au</span>
    </div>
  </section>
</body>
</html>
```